BRVE branded stationary template

We need associated stationary to accompany our new logo.

The stationary design will be used on business cards, presentation slides and document templates so needs to be provided in an EPS format so that we can adapt it. The design MUST BE ADAPTABLE.

The logo colour is #4a4195 or RGB 85/68/141. Associated colours that can be used in this stationary should compliment this colour. Other colour choices - the preference would be dark and light purples, blues, black and greys. Done how you see fit.

We want the stationary to compliment the overall design of the logo, so clean sharp lines are what we are looking for. It doesn't need to be overly intricate in design - something simple that compliments the look and feel of the logo is what we want. More focused on lines and shapes around the stationary, not any additional logos or pictures.

Target Market(s)

UK housing providers

Industry/Entity Type

Business

Font styles to use
Sans Serif

Requirements
Must have
• Clean sharp appearance, nothing overly elaborate.

```html
<!DOCTYPE html>
<html lang="en">
<head>
<meta charset="utf-8">
<title>BRVE Business Cards</title>
<link href="https://fonts.googleapis.com/css2?family=Arimo:wght@400;700&display=swap" rel="stylesheet">
<style>
  :root {
    --brand: #4a4195;
    --card-purple: #6861b2;
    --ink: #4a4a55;
    --rule: #cfcfd8;
    --paper: #ffffff;
    --backdrop: #e6e5ea;
  }
  * { margin: 0; padding: 0; box-sizing: border-box; }
  html, body { width: 1200px; height: 950px; overflow: hidden; }
  body {
    background: var(--backdrop);
    font-family: "Arimo", Arial, sans-serif;
    position: relative;
  }
  .card {
    position: absolute;
    width: 600px;
    height: 343px;
    box-shadow: 0 10px 28px rgba(0,0,0,0.18);
  }
  /* Front */
  .card-front {
    left: 150px; top: 80px;
    background: var(--card-purple);
    color: var(--paper);
  }
  .card-front .wordmark {
    position: absolute;
    left: 0; right: 0; top: 110px;
    text-align: center;
  }
  .brand-row { display: inline-flex; align-items: center; gap: 16px; }
  .brand-mark { width: 30px; height: 30px; background: currentColor; }
  .brand-name { font-size: 64px; font-weight: 700; letter-spacing: 2px; line-height: 1; }
  .tagline { font-size: 19px; margin-top: 8px; letter-spacing: 0.3px; }
  .card-front .url {
    position: absolute; left: 0; right: 0; top: 252px;
    text-align: center; font-size: 14px; letter-spacing: 5px;
  }
  /* Back */
  .card-back {
    left: 450px; top: 510px;
    background: var(--paper);
    color: var(--brand);
  }
  .card-back .wordmark { position: absolute; left: 40px; top: 125px; }
  .card-back .brand-name { font-size: 54px; }
  .card-back .brand-mark { width: 24px; height: 24px; }
  .card-back .tagline { font-size: 16px; }
  .divider {
    position: absolute; left: 352px; top: 30px; bottom: 30px;
    width: 1px; background: var(--rule);
  }
  .contact { position: absolute; left: 376px; top: 46px; color: var(--ink); }
  .person-name { font-size: 20px; font-weight: 700; color: var(--brand); }
  .person-role { font-size: 14px; margin-top: 3px; }
  .address { font-size: 14px; line-height: 1.35; margin-top: 12px; }
  .details { list-style: none; margin-top: 12px; }
  .details li {
    display: flex; align-items: center; gap: 10px;
    font-size: 14px; line-height: 1; margin-bottom: 8px;
  }
  .details svg { width: 14px; height: 14px; fill: var(--brand); flex: none; }
</style>
</head>
<body>
  <section class="card card-front">
    <div class="wordmark">
      <div class="brand-row"><span class="brand-mark"></span><span class="brand-name">BRVE</span></div>
      <p class="tagline">fresh thinking for better homes</p>
    </div>
    <p class="url">www.brvehome.com</p>
  </section>

  <section class="card card-back">
    <div class="wordmark">
      <div class="brand-row"><span class="brand-mark"></span><span class="brand-name">BRVE</span></div>
      <p class="tagline">fresh thinking for better homes</p>
    </div>
    <div class="divider"></div>
    <div class="contact">
      <p class="person-name">Alan Mercer</p>
      <p class="person-role">President</p>
      <p class="address">2710 Harrow Lane<br>Elm Ridge, NY 11320</p>
      <ul class="details">
        <li><svg viewBox="0 0 16 16"><path d="M3 2h3l1.5 3.5-2 1.5a9 9 0 0 0 3.5 3.5l1.5-2L14 10v3a1 1 0 0 1-1 1A11 11 0 0 1 2 3a1 1 0 0 1 1-1z"/></svg>514 2290 6631</li>
        <li><svg viewBox="0 0 16 16"><path d="M4.5 1h7a1 1 0 0 1 1 1v12a1 1 0 0 1-1 1h-7a1 1 0 0 1-1-1V2a1 1 0 0 1 1-1zm1 2v9h5V3z"/></svg>732 4418 0927</li>
        <li><svg viewBox="0 0 16 16"><path d="M4 1h6l2 2v3H4zM2 7h12a1 1 0 0 1 1 1v5H1V8a1 1 0 0 1 1-1zm2 3v2h8v-2z"/></svg>845 3176 2048</li>
        <li><svg viewBox="0 0 16 16"><path d="M1 3h14v10H1zm1.5 1.3V5l5.5 4 5.5-4v-.7z"/></svg>alan@brvehome.com</li>
        <li><svg viewBox="0 0 16 16"><circle cx="8" cy="8" r="7"/><path d="M1 8h14M8 1v14" stroke="#fff" stroke-width="1"/></svg>www.brvehome.com</li>
      </ul>
    </div>
  </section>
</body>
</html>
```